Exciting business card design for diesel performance and offroad business!!

We need a business card design that looks good and stands out. I don't want a plain old boring business card that you forget about and throw away at the end of the day. We are a diesel performance and truck accessory business that sell and install the industries biggest brands and best parts out there!

Industry/Entity Type

Business

Contact Information for Business Card

Dalton Prewick (Owner) 260-587-3146
bramble.motorworks@postmoor.com
Truck and Off-Road Performance and Accessories

Requirements
Must have
• A great look and feel about it. My logo needs to be in center of the card just like the attached picture. On the back I want it to have a list of items we offer
• Truck and Rovex: Lift and Leveling Kits, Intake and Exhaust Systems, Custom Tuning, Wheels and Tires, Steps, Bed Covers, Floor Liners, Custom Lighting, Turbos and Piping, Gauges, Much More!
• UTV: Suspension, Roll Cage, Doors, Exhaust, Tuning, Turbo Kits, Stereo, Wheels/Tires, Custom Lighting, Clutching, Much More!!

```html
<!DOCTYPE html>
<html lang="en">
<head>
<meta charset="utf-8">
<title>Bramble Motorworks – Business Card</title>
<link href="https://fonts.googleapis.com/css2?family=Open+Sans:wght@400;600;700&family=Source+Sans+3:wght@400;600;700&display=swap" rel="stylesheet">
<style>
  :root {
    --stage-top: #2a2a2a;
    --stage-bottom: #050505;
    --card: #ffffff;
    --ink: #111111;
    --ink-soft: #555555;
    --rule: #8a8a8a;
  }
  * { margin: 0; padding: 0; box-sizing: border-box; }
  html, body { width: 1200px; height: 900px; overflow: hidden; }
  body {
    position: relative;
    background: linear-gradient(180deg, var(--stage-top) 0%, #161616 55%, var(--stage-bottom) 100%);
    font-family: "Source Sans 3", "Myriad Pro", sans-serif;
    color: var(--ink);
  }
  .card {
    position: absolute;
    top: 306px;
    height: 271px;
    background: var(--card);
    border-radius: 12px;
    overflow: hidden;
  }
  .card--front { left: 149px; width: 439px; }
  .card--back { left: 608px; width: 441px; height: 272px; text-align: center; }

  /* Front */
  .brand {
    position: absolute;
    left: 66px; top: 78px;
    width: 110px; height: 104px;
    display: flex; flex-direction: column; align-items: center; justify-content: center;
    gap: 6px;
  }
  .brand__mark { width: 14px; height: 14px; background: var(--ink); }
  .brand__name {
    font-family: "Source Sans 3", sans-serif;
    font-weight: 700;
    font-size: 15px;
    line-height: 1.1;
    letter-spacing: 0.5px;
    text-align: center;
    color: var(--ink);
  }
  .person { position: absolute; left: 201px; top: 77px; }
  .person__name {
    font-family: "Open Sans", sans-serif;
    font-weight: 600; font-size: 15px; line-height: 20px;
  }
  .person__role {
    font-family: "Open Sans", sans-serif;
    font-size: 12px; color: var(--ink-soft); line-height: 14px; padding-left: 1px;
  }
  .contact { position: absolute; left: 202px; top: 141px; list-style: none; }
  .contact li {
    display: flex; align-items: center; gap: 6px;
    font-family: "Open Sans", sans-serif;
    font-size: 12px; line-height: 16px; color: #333;
  }
  .contact svg { width: 10px; height: 10px; fill: var(--ink); }
  .tagline {
    position: absolute; left: 0; right: 0; top: 228px;
    display: flex; align-items: center; gap: 8px;
    font-size: 13px; white-space: nowrap;
  }
  .tagline::before { content: ""; width: 69px; border-top: 1px solid var(--rule); }
  .tagline::after { content: ""; flex: 1; border-top: 1px solid var(--rule); margin-left: 0; }

  /* Back */
  .offer__title {
    font-family: "Open Sans", sans-serif;
    font-weight: 600; font-size: 20px; margin-top: 30px; line-height: 26px;
  }
  .offer__group { margin-top: 20px; }
  .offer__group + .offer__group { margin-top: 17px; }
  .offer__heading { font-size: 15px; line-height: 18px; margin-bottom: 7px; }
  .offer__items { font-size: 13px; line-height: 16px; }
</style>
</head>
<body>
  <section class="card card--front" aria-label="Business card front">
    <div class="brand">
      <span class="brand__mark"></span>
      <span class="brand__name">BRAMBLE<br>MOTORWORKS</span>
    </div>
    <div class="person">
      <p class="person__name">Dalton Prewick</p>
      <p class="person__role">Owner</p>
    </div>
    <ul class="contact">
      <li>
        <svg viewBox="0 0 24 24" aria-hidden="true"><path d="M6.6 10.8a15.1 15.1 0 0 0 6.6 6.6l2.2-2.2a1 1 0 0 1 1-.25 11.4 11.4 0 0 0 3.6.57 1 1 0 0 1 1 1V20a1 1 0 0 1-1 1A17 17 0 0 1 3 4a1 1 0 0 1 1-1h3.5a1 1 0 0 1 1 1c0 1.25.2 2.45.57 3.57a1 1 0 0 1-.25 1z"/></svg>
        260-587-3146
      </li>
      <li>
        <svg viewBox="0 0 24 24" aria-hidden="true"><path d="M2 5h20v14H2z M2 5l10 7 10-7" /></svg>
        bramble.motorworks@postmoor.com
      </li>
    </ul>
    <p class="tagline">Truck and offroad performance and Accessories</p>
  </section>

  <section class="card card--back" aria-label="Business card back">
    <h2 class="offer__title">WE OFFER</h2>
    <div class="offer__group">
      <h3 class="offer__heading">TRUCK AND ROVEX</h3>
      <p class="offer__items">Lift and leveling kits | intake and exhaust systems | custom tuning<br>wheels and tires | steps | bed covers | floor liners<br>custom lighting | turbos | etc</p>
    </div>
    <div class="offer__group">
      <h3 class="offer__heading">UTV</h3>
      <p class="offer__items">Suspension | Roll Cage | doors | exhaust | tuning | turbo kits | stereo<br>wheels/tires | custom lighting | clutching | etc..</p>
    </div>
  </section>
</body>
</html>
```